Cake website needs a professional WordPress design makeover!

I need a wordpress design for my company called Velvet Crumbhouse. It's a home cake business and I specialise in everything from cupcakes, celebratory cakes to couture wedding cakes. I have an existing one page wordpress website www.velvetcrumbhouse.example but it doesn't quite communicate elegance or showcase my skills so it desperately needs a complete change.

I purchased this theme
http://lumatheme.example/demos/themes/?product=vela
I basically want my website to look EXACTLY like this. I would obviously provide pictures of my work. I like the positioning of the pictures and texts and how each section are divided with the pictures. I also like the pop up of the welcome text on the home page. I would like that to say Welcome Velvet Crumbhouse.

One element I would like to keep from my original website are the slides on the home page. But will have a different caption with each slide. I will provide the three pictures for these slides.

The page format should be as follows:

Home
Discover Our Story
Tasteful Delights (Picture)
Discover Our Cakes - Clickable link below description going to the full cake menu with prices
The Perfect Blend (Picture)
Our Promise
Discover Your Special Day (Picture)
Wedding Cakes
Make an Order (Picture)
Get in touch

The menu on top of the page should read
Home, Our story, Our Cakes, Price List, Wedding cakes, Get in Touch

I would like to see the page of the full cake menu with the prices.
Signature colours Black, White and Pink

Target Market(s)

My main audience is targeted at women.

Industry/Entity Type

Wedding

Requirements
Must have
• Must look like the link I provided. Please use this as reference.
Nice to have
• Nice to see aspects of my logo, example the butterflies or the paisley design be subtly used around the website.

```html
<!DOCTYPE html>
<html lang="en">
<head>
<meta charset="utf-8">
<title>Velvet Crumbhouse</title>
<link rel="stylesheet" href="https://fonts.googleapis.com/css2?family=Open+Sans:wght@400;600;700&family=Raleway:wght@400;500&display=swap">
<style>
  :root {
    --rose: #c48580;
    --rose-deep: #b86f6a;
    --rose-text: #c57770;
    --ink: #2b2b2b;
    --body: #8a7f7c;
    --white: #ffffff;
    --footer: #161616;
    --cocoa: #5a3f3b;
    --field: #ffffff;
  }
  * { box-sizing: border-box; margin: 0; padding: 0; }
  html, body { width: 1200px; height: 2168px; overflow: hidden; }
  body {
    position: relative;
    background: var(--white);
    font-family: "Open Sans", Arial, sans-serif;
    color: var(--body);
  }

  /* Header */
  .site-header {
    position: absolute; left: 0; top: 0; width: 1200px; height: 600px;
    background: var(--rose);
  }
  .brand {
    position: absolute; left: 112px; top: 36px;
    display: flex; align-items: center; gap: 14px;
  }
  .brand-mark {
    width: 52px; height: 52px; border-radius: 50%;
    background: var(--white);
  }
  .brand-name {
    font-family: "Raleway", sans-serif; font-weight: 500;
    font-size: 25px; color: var(--white); white-space: nowrap;
  }
  .main-nav {
    position: absolute; right: 172px; top: 63px;
    display: flex; gap: 28px;
  }
  .main-nav a {
    font-size: 13px; color: var(--white); text-decoration: none; font-weight: 600;
    white-space: nowrap;
  }
  .search-btn {
    position: absolute; left: 1050px; top: 48px; width: 50px; height: 50px;
    background: #3a2f2e; display: flex; align-items: center; justify-content: center;
  }

  /* Slider */
  .hero-slider {
    position: absolute; left: 100px; top: 150px; width: 1000px; height: 508px;
  }
  .hero-slide {
    width: 100%; height: 100%;
    background: radial-gradient(circle at 30% 40%, #5a3a2c 0%, #7b4e3d 22%, transparent 40%),
                radial-gradient(circle at 75% 55%, #f2b3c2 0%, #e98aa4 25%, transparent 45%),
                linear-gradient(135deg, #e9c8cf 0%, #c58f92 40%, #6b4436 75%, #e7a7b6 100%);
  }
  .slider-arrow {
    position: absolute; top: 378px; width: 36px; height: 44px;
    background: #2b2b2b; display: flex; align-items: center; justify-content: center;
  }
  .slider-arrow.prev { left: 100px; }
  .slider-arrow.next { left: 1064px; }
  .slider-dots {
    position: absolute; left: 0; width: 1200px; top: 638px;
    display: flex; justify-content: center; gap: 8px;
  }
  .slider-dots span { width: 10px; height: 10px; border-radius: 50%; background: rgba(255,255,255,0.6); }
  .slider-dots span.active { background: var(--white); }

  /* Story */
  .section-title {
    font-family: "Raleway", sans-serif; font-weight: 400;
    color: var(--rose-text); font-size: 38px; line-height: 46px;
  }
  .story-text {
    position: absolute; left: 110px; top: 690px; width: 470px; text-align: center;
  }
  .story-text p, .wedding-text p { font-size: 13.5px; line-height: 22px; margin-top: 16px; }
  .text-link {
    display: inline-block; margin-top: 40px; font-size: 15px; color: var(--rose-text);
    letter-spacing: 1px; text-decoration: none;
  }
  .photo { position: absolute; }
  .story-photo-1 { left: 592px; top: 700px; width: 240px; height: 340px;
    background: linear-gradient(180deg, #f6eee8 0%, #f1d7c9 40%, #e7b9a3 65%, #eae6e2 100%); }
  .story-photo-2 { left: 860px; top: 700px; width: 240px; height: 340px;
    background: linear-gradient(180deg, #efe7e4 0%, #e7b3b0 45%, #d99b96 70%, #efe4e1 100%); }

  /* Cakes band */
  .cakes-band {
    position: absolute; left: 0; top: 1100px; width: 1200px; height: 220px;
    background: linear-gradient(90deg, #c79a93 0%, #e9d6cf 35%, #f2e7e0 55%, #d7aea6 80%, #b98680 100%);
    text-align: center;
  }
  .cakes-band h2 {
    margin-top: 44px; font-family: "Raleway", sans-serif; font-weight: 500;
    font-size: 38px; color: var(--white);
  }
  .btn-rose {
    display: inline-block; margin-top: 20px; width: 232px; height: 60px; line-height: 60px;
    background: var(--rose-deep); color: var(--white); font-size: 15px; text-decoration: none;
  }

  /* Wedding */
  .wedding-photo { width: 200px; height: 160px; }
  .wp-1 { left: 100px; top: 1380px; background: linear-gradient(160deg, #3a2620, #c0494a 50%, #f1e4dc); }
  .wp-2 { left: 320px; top: 1380px; background: linear-gradient(180deg, #e65a7b, #f2b33d 40%, #6cc16a 65%, #5f8fe0); }
  .wp-3 { left: 100px; top: 1560px; background: radial-gradient(circle, #f2c334 0%, #e24a5b 40%, #4a8fd6 70%, #2c2c2c 100%); }
  .wp-4 { left: 320px; top: 1560px; background: linear-gradient(160deg, #f6efe9, #e8a6b4 50%, #4a3530); }
  .wedding-text {
    position: absolute; left: 560px; top: 1440px; width: 540px; text-align: center;
  }
  .wedding-text .read-more {
    display: inline-block; margin-top: 24px; font-size: 15px; color: var(--ink);
    font-weight: 600; text-decoration: none;
  }

  /* Contact */
  .contact-band {
    position: absolute; left: 0; top: 1760px; width: 1200px; height: 260px;
    background: linear-gradient(90deg, #b4474a 0%, #e8898a 30%, #f3c3bf 55%, #d46a6d 80%, #a33c40 100%);
  }
  .contact-band h2 {
    position: absolute; left: 0; width: 1200px; top: 26px; text-align: center;
    font-family: "Raleway", sans-serif; font-weight: 500; font-size: 26px; color: var(--white);
  }
  .field {
    position: absolute; height: 64px; background: var(--field);
    padding: 0 14px; line-height: 64px; font-size: 13px; color: #555;
  }
  .f-name { left: 100px; top: 88px; width: 320px; }
  .f-phone { left: 432px; top: 88px; width: 320px; }
  .f-email { left: 772px; top: 88px; width: 328px; }
  .f-message { left: 100px; top: 172px; width: 652px; height: 60px; line-height: 60px; }
  .btn-submit {
    position: absolute; left: 772px; top: 172px; width: 328px; height: 60px;
    background: var(--cocoa); color: var(--white); font-weight: 700; font-size: 14px;
    text-align: center; line-height: 60px; letter-spacing: 1px;
  }

  /* Footer */
  .site-footer {
    position: absolute; left: 0; top: 2020px; width: 1200px; height: 148px;
    background: var(--footer); color: #bdbdbd; font-size: 12px;
  }
  .footer-links { position: absolute; left: 100px; top: 60px; }
  .footer-copy { position: absolute; left: 100px; top: 88px; }
  .social {
    position: absolute; left: 976px; top: 62px; display: flex; gap: 6px;
  }
  .social span { width: 20px; height: 20px; background: #3b5b93; }
  .social span:nth-child(2) { background: #3aa3d9; }
  .social span:nth-child(3) { background: #3a6ea8; }
  .social span:nth-child(4) { background: #5a5a5a; }
</style>
</head>
<body>

<header class="site-header">
  <div class="brand">
    <span class="brand-mark"></span>
    <span class="brand-name">Velvet Crumbhouse</span>
  </div>
  <nav class="main-nav">
    <a href="#">Home</a>
    <a href="#">Our story</a>
    <a href="#">Our Cakes</a>
    <a href="#">Price List</a>
    <a href="#">Wedding cakes</a>
    <a href="#">Get in Touch</a>
  </nav>
  <div class="search-btn">
    <svg width="20" height="20" viewBox="0 0 20 20"><circle cx="8" cy="8" r="6" fill="none" stroke="#fff" stroke-width="2"/><line x1="12.5" y1="12.5" x2="18" y2="18" stroke="#fff" stroke-width="2.4"/></svg>
  </div>
</header>

<section class="hero-slider">
  <div class="hero-slide" role="img" aria-label="Slide photo: close-up of chocolate and pink-sprinkled cake pops on a cooling rack"></div>
</section>
<div class="slider-arrow prev"><svg width="12" height="18" viewBox="0 0 12 18"><polyline points="9,2 3,9 9,16" fill="none" stroke="#fff" stroke-width="2.5"/></svg></div>
<div class="slider-arrow next"><svg width="12" height="18" viewBox="0 0 12 18"><polyline points="3,2 9,9 3,16" fill="none" stroke="#fff" stroke-width="2.5"/></svg></div>
<div class="slider-dots"><span class="active"></span><span></span><span></span></div>

<section class="story-text">
  <h2 class="section-title">Our Story</h2>
  <p>Every cake begins in our home kitchen with butter, patience and a love of fine detail. From playful cupcakes to towering celebration cakes, each piece is baked fresh, finished by hand and designed around your occasion, so the table looks as beautiful as it tastes and the memory lasts long after.</p>
  <a class="text-link" href="#">ABOUT US</a>
</section>
<div class="photo story-photo-1" role="img" aria-label="Photo of a cream layered cake on a glass stand"></div>
<div class="photo story-photo-2" role="img" aria-label="Photo of a pink lace-piped wedding cake on a glass stand"></div>

<section class="cakes-band" role="img" aria-label="Soft-focus background photo of cakes">
  <h2>Our Cakes</h2>
  <a class="btn-rose" href="#">Click Here</a>
</section>

<div class="photo wedding-photo wp-1" role="img" aria-label="Photo of a chocolate cake topped with berries"></div>
<div class="photo wedding-photo wp-2" role="img" aria-label="Photo of a rainbow layered cake slice"></div>
<div class="photo wedding-photo wp-3" role="img" aria-label="Photo of a cake covered in colourful sweets"></div>
<div class="photo wedding-photo wp-4" role="img" aria-label="Photo of a decorated celebration cake"></div>
<section class="wedding-text">
  <h2 class="section-title">Wedding Cakes</h2>
  <p>Couture wedding cakes shaped around your day, your colours and your story. We begin with a relaxed tasting, sketch ideas together and refine every tier, flower and ribbon until it feels entirely yours, then deliver and set it up so you can simply enjoy the celebration with the people you love.</p>
  <a class="read-more" href="#">Read more</a>
</section>

<section class="contact-band" role="img" aria-label="Soft-focus background photo of red and pink cakes">
  <h2>Get in Touch</h2>
  <div class="field f-name">Name</div>
  <div class="field f-phone">Phone</div>
  <div class="field f-email">Email</div>
  <div class="field f-message">Message</div>
  <div class="btn-submit">SUBMIT</div>
</section>

<footer class="site-footer">
  <div class="footer-links">Lumen Studio Inc | Terms | Privacy | Contact Us</div>
  <div class="footer-copy">© 2014 Company Name. All right reserved. Terms of Use</div>
  <div class="social"><span></span><span></span><span></span><span></span></div>
</footer>

</body>
</html>
```